Bright Anchor: Walking Past the Old Door

Religious genre. 6x9 book cover design for a new book that will also eventually be made into a workbook. Summary: Learn how God created you to be part of His Story of Grace so that you can flourish in your new identity in Him. This book explores how the story of the gospel informs our stories, how to live a new and free life by utilizing the 3 dimensions of the Gospel, and overcome how our former life has dominated us.

Target Market(s)

church members, church leaders

Industry/Entity Type

Religion

Colors
ffffff

Requirements
Must have
• White background with red and black print, clean, not too busy, easy-to-read design and font choices
Nice to have
• Play off the idea of the word "Bright" ... like vital signs or vitality

```html
<!DOCTYPE html>
<html lang="en">
<head>
<meta charset="utf-8">
<title>Walking Past the Old Door — Book Cover</title>
<link rel="stylesheet" href="https://fonts.googleapis.com/css2?family=Cinzel:wght@400;500&display=swap">
<style>
  :root {
    --page-bg: #e9e9e7;
    --cover-white: #ffffff;
    --cover-mist: #f1f1f0;
    --cover-teal: #8fcfcf;
    --cover-smoke: #3b3a38;
    --ink-black: #141414;
    --ink-red: #c8191e;
  }

  html, body {
    margin: 0;
    padding: 0;
    width: 1200px;
    height: 900px;
    overflow: hidden;
    background: var(--page-bg);
  }

  .canvas {
    position: relative;
    width: 1200px;
    height: 900px;
  }

  .book-cover {
    position: absolute;
    left: 312px;
    top: 40px;
    width: 576px;
    height: 820px;
    background: var(--cover-white);
    overflow: hidden;
    box-shadow: 0 6px 24px rgba(0, 0, 0, 0.18);
  }

  .cover-texture {
    position: absolute;
    inset: 0;
    background:
      radial-gradient(ellipse 70% 30% at 85% 82%, rgba(59, 58, 56, 0.35), transparent 70%),
      radial-gradient(ellipse 60% 35% at 10% 55%, rgba(143, 207, 207, 0.35), transparent 70%),
      linear-gradient(to bottom, var(--cover-white) 0%, var(--cover-mist) 55%, rgba(143, 207, 207, 0.55) 88%, var(--cover-teal) 100%);
  }

  .cover-title {
    position: absolute;
    left: 0;
    right: 0;
    top: 48px;
    margin: 0;
    text-align: center;
    font-family: "Cinzel", serif;
    font-weight: 400;
    color: var(--ink-black);
    line-height: 1;
  }

  .title-line {
    display: block;
  }

  .title-line--small {
    font-size: 50px;
    margin-bottom: 12px;
  }

  .title-line--large {
    font-size: 66px;
    margin-bottom: 12px;
  }

  .cover-emblem {
    position: absolute;
    left: 140px;
    top: 290px;
    width: 286px;
    height: 256px;
    border-radius: 50%;
    background: radial-gradient(circle at 50% 55%, var(--ink-black) 0%, var(--ink-black) 30%, var(--ink-red) 58%, rgba(200, 25, 30, 0) 72%);
  }

  .cover-author {
    position: absolute;
    left: 0;
    right: 0;
    top: 738px;
    margin: 0;
    text-align: center;
    font-family: "Cinzel", serif;
    font-weight: 400;
    font-size: 36px;
    letter-spacing: 0.18em;
    color: var(--ink-black);
  }
</style>
</head>
<body>
  <main class="canvas">
    <section class="book-cover">
      <div class="cover-texture" role="img" aria-label="Soft white marble texture fading into pale teal and dark smoky stains toward the bottom"></div>

      <h1 class="cover-title">
        <span class="title-line title-line--small">Walking</span>
        <span class="title-line title-line--large">Past the Old</span>
        <span class="title-line title-line--small">Door</span>
      </h1>

      <div class="cover-emblem" role="img" aria-label="Interlaced red and black knot emblem with a heart at its centre"></div>

      <p class="cover-author">AUTOR NAME</p>
    </section>
  </main>
</body>
</html>
```